Engineering/Manufacturing Company Needs PowerPoint Update and Template

We want to update the look and feel of our current corporate overview PowerPoint. We would like a working template moving forward with 6-8 slide layouts as well as a couple cover page options. Our content ranges from basic bullet points to complex graphs, images, and a combination of those, so we need templates that will work with a wide variety of content.
Our company specializes in complex precision machining, Engineering, and Advanced heavy duty truck products. We would like this presentation to represent our high-level manufacturing technology.
Our corporate color is blue (RBG 26/75/159), and we also use gray and white. We are looking for a modern, clean, yet masculine/industrial feeling. I have included our company logo, but other than that we would like to see what you can come up with. We would like it to feel clean yet industrial.
Target Market(s)
High-level management in the manufacturing and heavy duty truck/bus industries.
Industry/Entity Type
Manufacturer

```html
<!DOCTYPE html>
<html lang="en">
<head>
<meta charset="UTF-8">
<title>Cover Slide – Project Title</title>
<link href="https://fonts.googleapis.com/css2?family=Oswald:wght@500;700&display=swap" rel="stylesheet">
<style>
  :root {
    --brand-blue: #1a4b9f;
    --brand-blue-deep: #123a86;
    --brand-blue-light: #3f72c9;
    --accent-sky: #9cc0f2;
    --paper: #ffffff;
    --steel-gray: #5d6168;
    --metal-light: #e8eef8;
    --metal-mid: #b3c6e6;
    --metal-edge: #7f9fd3;
  }
  * { margin: 0; padding: 0; box-sizing: border-box; }
  html, body {
    width: 1200px;
    height: 900px;
    overflow: hidden;
    background: var(--paper);
  }
  .slide {
    position: relative;
    width: 1200px;
    height: 900px;
    overflow: hidden;
    background: var(--paper);
    font-family: "Oswald", "Arial Narrow", sans-serif;
  }
  .slide__backdrop {
    position: absolute;
    inset: 0;
    width: 1200px;
    height: 900px;
  }
  .slide__product-image {
    position: absolute;
    left: 32px;
    top: 350px;
    width: 490px;
    height: 365px;
    border-radius: 32px;
    background: radial-gradient(ellipse at 40% 40%, var(--metal-light) 0%, var(--metal-mid) 60%, var(--metal-edge) 100%);
    box-shadow: 0 10px 28px rgba(18, 58, 134, 0.25);
  }
  .slide__title-block {
    position: absolute;
    right: 75px;
    top: 345px;
    text-align: right;
    color: var(--paper);
    text-transform: uppercase;
  }
  .slide__title {
    font-weight: 700;
    font-size: 62px;
    line-height: 1.1;
    letter-spacing: 0;
  }
  .slide__subtitle {
    margin-top: 6px;
    font-weight: 700;
    font-size: 30px;
    line-height: 1.2;
    letter-spacing: 0.5px;
  }
  .brand-signature {
    position: absolute;
    right: 78px;
    top: 700px;
    text-align: right;
  }
  .brand-signature__name {
    font-weight: 700;
    font-size: 104px;
    line-height: 1;
    color: var(--brand-blue);
    letter-spacing: 2px;
  }
  .brand-signature__tagline {
    margin-top: 4px;
    font-weight: 500;
    font-size: 26px;
    color: var(--steel-gray);
    letter-spacing: 2px;
    text-transform: uppercase;
  }
  .slide__footer-band {
    position: absolute;
    left: 0;
    bottom: 0;
    width: 1200px;
    height: 35px;
    background: var(--brand-blue);
  }
</style>
</head>
<body>
  <main class="slide">
    <svg class="slide__backdrop" viewBox="0 0 1200 900" aria-hidden="true">
      <defs>
        <linearGradient id="header-fill" x1="0" y1="0" x2="1" y2="1">
          <stop offset="0" stop-color="#1d55b0"/>
          <stop offset="0.5" stop-color="#1a4b9f"/>
          <stop offset="1" stop-color="#2a5fbd"/>
        </linearGradient>
      </defs>
      <path class="accent-swoosh" d="M0,590 C320,660 700,700 1200,600 L1200,628 C720,712 330,680 0,600 Z" fill="var(--accent-sky)"/>
      <path class="header-field" d="M0,0 L1200,0 L1200,590 C720,680 330,650 0,578 Z" fill="url(#header-fill)"/>
    </svg>

    <div class="slide__product-image" role="img" aria-label="Photograph of a machined aluminium truck component with braided wiring harness"></div>

    <header class="slide__title-block">
      <h1 class="slide__title">Project Title Here</h1>
      <p class="slide__subtitle">Subtext Here</p>
    </header>

    <div class="brand-signature">
      <div class="brand-signature__name">KELTRA</div>
      <div class="brand-signature__tagline">Precision in Motion</div>
    </div>

    <div class="slide__footer-band"></div>
  </main>
</body>
</html>
```